Modern brochure by Lawyers, for modern clients

It'sa "News" for their clients. Attached you can find the current News without design. It must be elegant but very attractive and modern. Their web site is http://www.montealtoyasociados.cl/ Their expertise is labor and employment practice area. It must be in editable format so that lawyers can write the news in a template with this corporate design.

Target Market(s)

Big Companies

Font styles to use
Sans Serif

Colors
0255a3
474747

Requirements
Nice to have
• Legal Pictures and only a little of yellow. One touch! It must be in editable format so that lawyers can write the news in a template with this corporate design.

```html
<!DOCTYPE html>
<html lang="es">
<head>
<meta charset="utf-8">
<title>Montealto y Asociados — Noticias</title>
<link rel="stylesheet" href="https://fonts.googleapis.com/css2?family=Lato:wght@400;700&display=swap">
<style>
  :root{
    --navy:#3b5675;
    --steel:#7b96a6;
    --mist:#aac0cc;
    --ice:#d6e2e8;
    --ink:#1f1f1f;
    --gray:#8a8a8a;
    --paper:#ffffff;
    --sky-top:#2f5fa8;
    --sky-bottom:#6f8fb8;
  }
  *{margin:0;padding:0;box-sizing:border-box}
  html,body{width:887px;height:1200px;overflow:hidden;background:var(--paper)}
  body{font-family:'Lato',sans-serif;color:var(--ink);position:relative}
  .top-rule{position:absolute;left:0;top:0;width:887px;height:10px;background:var(--navy)}

  .firm-name{position:absolute;font-weight:400;color:var(--navy);white-space:nowrap}
  .header-name{left:51px;top:62px;font-size:30px}
  .issue-date{position:absolute;right:40px;top:86px;font-size:16.5px;color:var(--gray);letter-spacing:-.2px}

  .hero-side{position:absolute;left:0;top:149px;width:61px;height:342px;background:var(--navy)}
  .hero{position:absolute;left:109px;top:146px;width:778px;height:341px}
  .hero svg{position:absolute;inset:0}
  .hero-title{position:absolute;left:43px;top:95px;color:#fff;font-weight:700;font-size:30px;letter-spacing:.3px}
  .hero-title::after{content:"";position:absolute;left:0;top:47px;width:257px;height:2px;background:#fff}
  .hero-lead{position:absolute;left:43px;top:158px;width:422px;color:#fff;font-weight:700;font-size:19.4px;line-height:24.5px}

  .stripe{position:absolute;height:7px;display:flex}
  .stripe span{flex:1}
  .stripe-body{left:116px;top:537px;width:258px}
  .stripe-body span:nth-child(1){background:var(--navy)}
  .stripe-body span:nth-child(2){background:var(--steel)}
  .stripe-body span:nth-child(3){background:var(--mist)}
  .stripe-body span:nth-child(4){background:var(--ice)}

  .article{position:absolute;left:114px;top:562px;width:726px;font-size:16.3px;line-height:20.8px}
  .article p{margin-bottom:18px}
  .article .intro{font-weight:700;width:640px}

  .closing{position:absolute;left:0;top:858px;width:820px;height:216px;background:var(--navy);color:#fff}
  .closing-side{position:absolute;left:847px;top:858px;width:40px;height:216px;background:var(--navy)}
  .closing p{position:absolute;left:114px;font-size:19.2px;line-height:23.5px;font-weight:400;width:480px}
  .closing .more{top:38px}
  .closing .signoff{top:133px;width:600px}
  .stripe-closing{left:183px;top:176px;width:191px;height:6px}
  .stripe-closing span:nth-child(1){background:var(--steel)}
  .stripe-closing span:nth-child(2){background:var(--mist)}
  .stripe-closing span:nth-child(3){background:var(--ice)}

  .site{position:absolute;left:0;width:887px;top:1089px;text-align:center;font-weight:700;font-size:16px;color:var(--navy)}
  .footer-name{left:0;width:887px;top:1138px;text-align:center;font-size:18px}
</style>
</head>
<body>
  <div class="top-rule"></div>

  <header>
    <p class="firm-name header-name">Montealto y Asociados</p>
    <p class="issue-date">Santiago, 25 de julio de 2018</p>
  </header>

  <div class="hero-side"></div>
  <section class="hero">
    <svg width="778" height="341" viewBox="0 0 778 341">
      <defs>
        <linearGradient id="sky" x1="0" y1="0" x2="0" y2="1">
          <stop offset="0" stop-color="#2f5fa8"/>
          <stop offset=".75" stop-color="#6f8fb8"/>
          <stop offset="1" stop-color="#5c7a3c"/>
        </linearGradient>
      </defs>
      <rect width="778" height="341" fill="#3b5675"/>
      <polygon role="img" aria-label="Fotografía de un edificio corporativo de fachada de cristal con árboles" points="426,0 778,0 778,337 398,337 507,171" fill="url(#sky)"/>
    </svg>
    <h1 class="hero-title">ESTIMADOS,</h1>
    <p class="hero-lead">Por medio del presente, les damos a conocer el Dictamen Ordinario N° 3826-031, emitido por la Dirección del Trabajo el pasado 20 de julio, relativo a los “beneficios históricos”.</p>
  </section>

  <div class="stripe stripe-body"><span></span><span></span><span></span><span></span></div>

  <article class="article">
    <p class="intro">Estos fueron definidos en su oportunidad por este organismo como “…aquellos beneficios que se han otorgado desde siempre…” por parte del empleador.</p>
    <p>A partir de este Dictamen, el cual reconsidera el criterio del anterior Director del Trabajo, los beneficios históricos vuelven a ser patrimonio de la empresa y de los trabajadores que los han recibido, dejando de serlo de la organización sindical y de sus socios beneficiados por el solo hecho de haberse “replicado” en un instrumento colectivo durante una negociación.</p>
    <p>Por último, el Dictamen en comento aclara que si un “beneficio histórico” se incrementa de manera real y efectiva producto de una negociación colectiva, únicamente dicho incremento se entenderá originado en el respectivo instrumento colectivo, y en consecuencia, objeto de una posible extensión en el evento de que ésta se haya acordado durante la negociación.</p>
  </article>

  <section class="closing">
    <p class="more">Para mayor análisis de lo resuelto por la Dirección del Trabajo, se puede revisar el Dictámen en comento haciendo click aquí</p>
    <p class="signoff">Sin otro particular saluda atentamente a usted</p>
    <div class="stripe stripe-closing"><span></span><span></span><span></span></div>
  </section>
  <div class="closing-side"></div>

  <footer>
    <p class="site">www.montealtoyasociados.cl</p>
    <p class="firm-name footer-name">Montealto y Asociados</p>
  </footer>
</body>
</html>
```